Book Cover Design Project

I have written a booK called "keep the lamp Lit:
a guide to starting and running a small business. It is aimed at the start up entrepreneur and seeks to give them everything they need to start up and run a small business. I am interested in a very simple cover that is contemporary in the look but clearly communicates the mission of the book. It should sell very well as there are no others like it, so the designer will get excellent exposure.
Updates

Reason: I an vacation in Europe until the 23rd of July. Would like a few days to make a decision after my return Walt

We are currently on vacation.  Will make a final decision in about a week.  Thanks so much for your submissions

Walt

Target Market(s)

Start up businesses in the U.S.

Industry/Entity Type

Business

Requirements
Must have
• Clear communication of the name. Lots of white space. Graphic communication of the purpose of the book? Prominent exposure of my name. Walter j. Pennick

```html
<!DOCTYPE html>
<html lang="en">
<head>
<meta charset="utf-8">
<title>Keep the Lamp Lit — Walter J. Pennick</title>
<link rel="stylesheet" href="https://fonts.googleapis.com/css2?family=Anton&family=Oswald:wght@400&family=Questrial&display=swap">
<style>
  :root {
    --navy: #0a2a78;
    --author-blue: #1414ff;
    --title-ink: #050505;
    --subtitle: #ffffff;
    --sky-top: #6f93c4;
    --sky-mid: #c9d8e8;
    --horizon: #a59a6c;
    --road: #4a4c4f;
  }
  html, body {
    margin: 0;
    padding: 0;
    width: 800px;
    height: 1200px;
    overflow: hidden;
    background: #ffffff;
  }
  .cover {
    position: relative;
    width: 800px;
    height: 1200px;
    overflow: hidden;
    background: var(--navy);
  }
  .author-band {
    position: absolute;
    left: 0; top: 0;
    width: 800px; height: 233px;
    background: var(--navy);
  }
  .author-name {
    display: block;
    width: 800px;
    height: 233px;
  }
  .author-name text {
    font-family: "Anton", "Impact", sans-serif;
    fill: var(--author-blue);
  }
  .scene {
    position: absolute;
    left: 0; top: 233px;
    width: 800px; height: 816px;
    background: linear-gradient(to bottom,
      var(--sky-top) 0%,
      var(--sky-mid) 35%,
      #dfe7ee 52%,
      var(--horizon) 56%,
      #6d6a55 62%,
      var(--road) 72%,
      #3d3f42 100%);
  }
  .title {
    position: absolute;
    left: 0; top: 490px;
    width: 800px; height: 170px;
  }
  .title text {
    font-family: "Oswald", "Arial Narrow", sans-serif;
    font-weight: 400;
    fill: var(--title-ink);
  }
  .subtitle {
    position: absolute;
    left: 140px; top: 735px;
    width: 600px;
    margin: 0;
    font-family: "Questrial", "Century Gothic", sans-serif;
    font-weight: 400;
    color: var(--subtitle);
    line-height: 1.08;
  }
  .subtitle span { display: block; }
  .subtitle em { font-style: italic; }
  .subtitle .line-1 { font-size: 37px; margin-left: 28px; }
  .subtitle .line-2 { font-size: 45px; margin-left: 72px; }
  .subtitle .line-3 { font-size: 53px; margin-left: 80px; }
  .subtitle .line-4 { font-size: 64px; margin-left: 0; }
  .subtitle .line-4 em { font-size: 72px; }
  .base-band {
    position: absolute;
    left: 0; top: 1049px;
    width: 800px; height: 151px;
    background: var(--navy);
  }
</style>
</head>
<body>
  <main class="cover">
    <header class="author-band">
      <svg class="author-name" viewBox="0 0 800 233" aria-label="Walter j. Pennick">
        <text x="48" y="158" font-size="112" textLength="705" lengthAdjust="spacingAndGlyphs">Walter j. Pennick</text>
      </svg>
    </header>

    <div class="scene" role="img" aria-label="Photograph of a straight open road running to the horizon through flat grassland under a blue sky with white clouds"></div>

    <svg class="title" viewBox="0 0 800 170" aria-label="Keep the Lamp Lit">
      <text x="70" y="148" font-size="168" textLength="702" lengthAdjust="spacingAndGlyphs">KEEP THE LAMP LIT</text>
    </svg>

    <p class="subtitle">
      <span class="line-1">A guide for</span>
      <span class="line-2"><em>Starting</em> and</span>
      <span class="line-3"><em>Running</em> a</span>
      <span class="line-4"><em>Small</em> Business</span>
    </p>

    <footer class="base-band"></footer>
  </main>
</body>
</html>
```